Overseas Property Tax Depreciation

We need a two sided flyer to promote our business and explain what we do. our website is www.tolbexmu.net.
The attached word file is what I would like on an A5 size flyer with one side showing the FAQ and the other the worked example. I would like these formatted much better than the are and in general style of the website. I will attach files for logos as well.

```html
<!DOCTYPE html>
<html lang="en">
<head>
<meta charset="utf-8">
<title>Farshore Tax Depreciation – Flyer</title>
<link href="https://fonts.googleapis.com/css2?family=Arimo:wght@400;700&family=Open+Sans:wght@400;600&family=Carlito:wght@400;700&display=swap" rel="stylesheet">
<style>
:root{
  --stage:#8b8b8b;
  --paper:#ffffff;
  --orange:#f7a21b;
  --orange-deep:#f08a12;
  --orange-light:#fcd24a;
  --green:#5ba632;
  --green-light:#9fcb3a;
  --green-dark:#3f8f2c;
  --ink:#1c1c1c;
  --rule:#8d8d8d;
}
*{margin:0;padding:0;box-sizing:border-box}
html,body{width:1200px;height:850px;overflow:hidden;background:var(--stage)}
.stage{position:relative;width:1200px;height:850px}
.page{position:absolute;top:60px;width:514px;height:725px;background:var(--paper);overflow:hidden}
.page--faq{left:83px}
.page--example{left:625px}

.top-band{position:absolute;top:36px;left:0;height:17px;background:var(--orange)}
.top-rule{position:absolute;top:56px;left:0;height:5px;background:var(--green)}
.page--faq .top-band,.page--faq .top-rule{width:355px}
.page--example .top-band,.page--example .top-rule{width:365px}

.brand{position:absolute;display:flex;align-items:center;gap:6px;font-family:Arimo,sans-serif;font-weight:700;font-size:12px;line-height:1;color:var(--ink);white-space:nowrap}
.brand__mark{width:10px;height:10px;background:var(--green)}
.page--faq .brand{top:40px;right:30px}
.page--example .brand{top:697px;right:30px}

.bottom-band{position:absolute;left:0;bottom:0;width:100%;height:50px;background:linear-gradient(90deg,var(--green-dark),var(--green) 55%,var(--green-light))}
.badge-member{position:absolute;left:10px;top:11px;width:72px;height:27px;border-radius:4px;background:#ffffff;opacity:.85}
.badge-register{position:absolute;right:14px;top:6px;width:36px;height:38px;border-radius:50%;background:#ffffff}

/* FAQ side */
.faq{position:absolute;top:66px;left:32px;width:452px;font-family:Arimo,sans-serif;font-size:9.3px;line-height:11.6px;color:var(--ink);text-align:justify}
.faq h2{font-family:"Open Sans",sans-serif;font-weight:400;font-size:17px;line-height:18px;color:var(--orange-deep);margin:9px 0 1px;text-align:left}
.faq h2:first-child{margin-top:0}
.faq p{margin:0}
.ticks{list-style:none}
.ticks li{position:relative;padding-left:10px}
.ticks li::before{content:"";position:absolute;left:1px;top:2px;width:3px;height:6px;border:solid var(--green);border-width:0 1.5px 1.5px 0;transform:rotate(40deg)}

/* Example side */
.example-title{position:absolute;top:35px;left:372px;font-family:Carlito,sans-serif;font-weight:700;font-size:9.5px;line-height:12px;color:var(--ink)}
.worked{position:absolute;top:92px;left:23px;width:471px;height:566px;border:3px solid var(--rule);border-collapse:collapse;table-layout:fixed;font-family:Carlito,sans-serif;font-size:10.4px;line-height:12px;color:var(--ink)}
.worked td,.worked th{padding:0 4px;vertical-align:middle;text-align:left;font-weight:400}
.worked .u{text-decoration:underline}
.worked th{font-size:9.5px}
.worked .c-ref{border-right:1px solid var(--rule)}
.worked .c-euro,.worked .c-aud{background:linear-gradient(90deg,var(--orange-deep),var(--orange) 40%,var(--orange-light));font-weight:700;font-size:10px}
.worked .c-aud{background:linear-gradient(90deg,var(--orange-light),#fde56a)}
.worked .c-with{background:linear-gradient(90deg,#8ec43c,var(--green));font-weight:700;font-size:10px}
.worked th.c-euro,.worked th.c-aud,.worked th.c-with{text-align:center;font-weight:700;font-size:8px;line-height:16px;padding:0 2px}
.worked tr.sec td{border-top:1px solid var(--rule)}
.worked tr.head td, .worked tr.head th{border-bottom:1px solid var(--rule)}
.worked .hl{color:#2e9a2e}
</style>
</head>
<body>
<div class="stage">

  <section class="page page--faq">
    <div class="top-band"></div>
    <div class="top-rule"></div>
    <div class="brand"><span class="brand__mark"></span><span class="brand__name">Farshore Tax Depreciation</span></div>

    <div class="faq">
      <h2>Why use us?</h2>
      <p>There are several websites out there offering tax depreciation reports for Australian properties but there are very few who are appropriately qualified and approved by the Australian Tax Office (ATO) and offer the necessary Irish expertise. The Quantity Surveyor that prepares your report:</p>
      <ul class="ticks">
        <li>is Irish and qualified as a Quantity Surveyor in Ireland.</li>
        <li>worked there during the ‘Celtic Tiger’ period when construction costs were quite high.</li>
        <li>has detailed knowledge of Irish construction methods and costs over the past 20 years. Irish buildings are generally much more expensive than Australia due to the climate, just think about how many Australian houses you have seen that have double glazing, central heating, insulation etc..</li>
        <li>has a partnership arrangement with an Irish quantity surveying firm to carry out the property inspections required in most cases to maximize the deductions available.</li>
        <li>is a chartered member of the CSIV.</li>
        <li>Maintains the Appropriate Professional Indemnity Insurance.</li>
        <li>Is registered with the Tax Practitioners Board. All quantity surveyors who prepare Property Tax Depreciation Schedules are required by the ATO to be registered with the Tax Practitioners Board which checks that the person preparing the reports is suitably qualified and maintains the appropriate professional indemnity insurance. You can check the registration on the TPB website. Our registration number is 31846027.</li>
      </ul>

      <h2>My property is in Ireland does this make a difference?</h2>
      <p>Division 43 of the Income Tax Assessment Act 1997 which deals with capital works depreciation states that it applies to buildings begun outside Australia after 21 August 1990 Sect 43.20 (1) (b). Your Australian tax return should cover your worldwide income. As long as the property is available to rent back in Ireland you are obliged by the ATO to report any income or loss on that property.</p>

      <h2>Is my property too old?</h2>
      <p>No, if your property was constructed after 1990 you can claim for both the construction cost element and the Plant and equipment. If it was built before then you can still claim the plant and equipment allowance. The easiest thing to do is to contact us with some details on your property and we can make an initial assessment of the possible annual savings.</p>

      <h2>What is Property Depreciation?</h2>
      <p>Just like you claim wear and tear on a car purchased for income producing purposes, you can also claim the depreciation of your investment property against your taxable income.</p>
      <p>There are 2 types available: depreciation on Plant and Equipment, and depreciation on the cost of construction. Plant and Equipment refers to items within the building like ovens, dishwashers, carpet and blinds etc. Both these costs can be offset against your assessable income.</p>

      <h2>How much will the report cost?</h2>
      <p>Each scenario is different so contact us to obtain a quick quote for your situation. Generally the cost of the report is a fraction of the savings in any one year.</p>
      <ul class="ticks">
        <li>Our fee is fully tax deductible</li>
        <li>You do NOT need to get this report done every year so the cost can be spread over several years</li>
      </ul>

      <h2>I haven't included my property for the past couple of years on my tax return is this a problem?</h2>
      <p>No, in actual fact you could have been missing out on savings for a number of years, you can also use this report to claim a refund from the ATO for up to the past three years.</p>
    </div>

    <div class="bottom-band">
      <div class="badge-member"></div>
      <div class="badge-register"></div>
    </div>
  </section>

  <section class="page page--example">
    <div class="top-band"></div>
    <div class="top-rule"></div>
    <div class="example-title">Property Tax Depreciation Example<br>3 bed Semi - detached house<br>Dublin, Constructed in 2006</div>

    <table class="worked">
      <colgroup>
        <col style="width:29px"><col style="width:166px"><col style="width:95px">
        <col style="width:48px"><col style="width:50px"><col style="width:83px">
      </colgroup>
      <tr class="head" style="height:56px">
        <th class="c-ref u">Ref</th>
        <th class="u" colspan="2">Description</th>
        <th class="c-euro" colspan="2" style="background:linear-gradient(90deg,var(--orange-deep),var(--orange-light))"><span class="u">Without Property</span><br><span class="u">Tax Depreciation</span><br><span class="u">Euro</span> &nbsp;&nbsp;&nbsp;&nbsp;&nbsp;&nbsp;&nbsp; <span class="u">AUD</span></th>
        <th class="c-with"><span class="u">With Property</span><br><span class="u">Depreciation Report</span><br><span class="u">AUD</span></th>
      </tr>
      <tr style="height:32px"><td class="c-ref u">A</td><td class="u">Rental Income</td><td><span class="u">€1,200</span> &nbsp;<span class="u">Month</span></td><td class="c-euro u">€14,400</td><td class="c-aud u">$20,571</td><td class="c-with u">$20,571</td></tr>
      <tr class="sec" style="height:20px"><td class="c-ref">-</td><td class="u">Expenses</td><td>-</td><td class="c-euro">-</td><td class="c-aud">-</td><td class="c-with">-</td></tr>
      <tr style="height:30px"><td class="c-ref u">B</td><td class="u">Annual Interest charged on outstanding Mortgage (4% apr)</td><td>-</td><td class="c-euro u">€12,040</td><td class="c-aud u">$17,200</td><td class="c-with u">$17,200</td></tr>
      <tr style="height:20px"><td class="c-ref u">C</td><td class="u">Property agent fees or commission</td><td>-</td><td class="c-euro u">€1,200</td><td class="c-aud u">$1,714</td><td class="c-with u">$1,714</td></tr>
      <tr style="height:18px"><td class="c-ref u">D</td><td class="u">Local Property Tax</td><td>-</td><td class="c-euro u">€250</td><td class="c-aud u">$357</td><td class="c-with u">$357</td></tr>
      <tr style="height:17px"><td class="c-ref u">E</td><td class="u">Repairs and Maintenance</td><td>-</td><td class="c-euro u">€2,000</td><td class="c-aud u">$2,857</td><td class="c-with u">$2,857</td></tr>
      <tr style="height:17px"><td class="c-ref u">F</td><td class="u">Home Insurance</td><td>-</td><td class="c-euro u">€450</td><td class="c-aud u">$643</td><td class="c-with u">$643</td></tr>
      <tr style="height:18px"><td class="c-ref u">G</td><td class="u">Cleaning Advertising et..</td><td>-</td><td class="c-euro u">€1,500</td><td class="c-aud u">$2,143</td><td class="c-with u">$2,143</td></tr>
      <tr style="height:19px"><td class="c-ref u hl">H</td><td class="u hl">Property Tax Depreciation</td><td class="hl">-</td><td class="c-euro u hl">€0</td><td class="c-aud u hl">$0</td><td class="c-with u hl">$15,000</td></tr>
      <tr class="sec" style="height:18px"><td class="c-ref u">I</td><td class="u">Total Annual Expenses</td><td class="u">Total (B to H)</td><td class="c-euro u">€17,440</td><td class="c-aud u">$24,914</td><td class="c-with u">$39,914</td></tr>
      <tr class="sec" style="height:20px"><td class="c-ref u">J</td><td class="u">Annual Rental Loss/Gain</td><td class="u">(A less I)</td><td class="c-euro u">-€3,040</td><td class="c-aud u">-$4,343</td><td class="c-with u">-$19,343</td></tr>
      <tr class="sec" style="height:38px"><td class="c-ref u">K</td><td class="u">Your Annual Income from other sources</td><td>-</td><td class="c-euro">-</td><td class="c-aud u">$180,000</td><td class="c-with u">$180,000</td></tr>
      <tr style="height:36px"><td class="c-ref u">L</td><td class="u">Tour Taxable Income after Rental Losses/Gains</td><td class="u">(K Plus J)</td><td class="c-euro">-</td><td class="c-aud u">$175,657</td><td class="c-with u">$160,657</td></tr>
      <tr style="height:16px"><td class="c-ref">-</td><td>-</td><td>-</td><td class="c-euro">-</td><td class="c-aud">-</td><td class="c-with">-</td></tr>
      <tr style="height:32px"><td class="c-ref u">M</td><td class="u">Your Marginal Income Tax Rate (37% +2% medicare)</td><td>- &nbsp;&nbsp;&nbsp;&nbsp;&nbsp;&nbsp;&nbsp;&nbsp;&nbsp; 39%</td><td class="c-euro">-</td><td class="c-aud">-</td><td class="c-with">-</td></tr>
      <tr class="sec" style="height:20px"><td class="c-ref u">N</td><td class="u">Annual Tax Saving</td><td class="u">(J multiplied by M)</td><td class="c-euro">-</td><td class="c-aud u">$1,694</td><td class="c-with u">$7,544</td></tr>
      <tr style="height:14px"><td class="c-ref">-</td><td class="u">Foreign Tax Credits</td><td>-</td><td class="c-euro">-</td><td class="c-aud">-</td><td class="c-with">-</td></tr>
      <tr style="height:30px"><td class="c-ref u">O</td><td class="u">Non-resident Landlord withholding Tax (20% Ireland)</td><td class="u">(A multiplied by 20%)</td><td class="c-euro u">€2,880</td><td class="c-aud u">$4,114</td><td class="c-with u">$4,114</td></tr>
      <tr style="height:20px"><td class="c-ref u">P</td><td class="u">Nett Tax Savings</td><td class="u">(N Plus O)</td><td class="c-euro">-</td><td class="c-aud u">$5,808</td><td class="c-with u">$11,658</td></tr>
      <tr class="sec" style="height:56px"><td class="c-ref u">Q</td><td class="u">Additional Money in your Pocket (Australia) per year due to Property Tax Depreciation</td><td>- &nbsp;&nbsp;&nbsp;&nbsp; -</td><td class="c-euro">-</td><td class="c-aud">-</td><td class="c-with u">$5,850</td></tr>
    </table>

    <div class="bottom-band"></div>
    <div class="brand"><span class="brand__mark"></span><span class="brand__name">Farshore Tax Depreciation</span></div>
  </section>

</div>
</body>
</html>
```